New Business Card for Casual Beachfront Cafe

Quirky Beachfront Cafe at Moana, South Australia needs a DOUBLE SIDED business card to print on PrintHarbor.

Target Market(s)

Business Cards sit on the counter for Guests to take with them. Please view our website www.saltreefcafe.com.au to get a feel for the Cafe. You may also view our Instagram at @saltreefcafe

Industry/Entity Type

Cafe / Restaurant

Contact Information for Business Card

Information equivalent to: Breakfast, Lunch, Dinner, Coffee, Takeaway / 117 Parade Coralby SA 5172 / Menu & Opening Hours: www.saltreefcafe.com.au / ph (08) 8461 9273

Requirements
Must have
• Information equivalent to: Breakfast, Lunch, Dinner, Coffee, Takeaway / 117 Parade Coralby SA 5172 / Menu & Opening Hours: www.saltreefcafe.com.au / ph (08) 8461 9273
Nice to have
• Potentially some of our trademark colours (Cafe can be searched via Seekly)
Should not have
• Must NOT have image of the building. May have the logo provided on one side but not necessarily, depending on how you wish to design the card

```html
<!DOCTYPE html>
<html lang="en">
<head>
<meta charset="utf-8">
<title>Salt Reef Cafe – Business Card</title>
<link href="https://fonts.googleapis.com/css2?family=Roboto:wght@700;900&display=swap" rel="stylesheet">
<style>
  :root{
    --yellow:#f2ea0c;
    --blue:#134a80;
    --orange:#b95a28;
    --ink:#111111;
    --page:#ffffff;
  }
  html,body{margin:0;padding:0;width:1200px;height:566px;overflow:hidden;background:var(--page);}
  .sheet{position:relative;width:1200px;height:566px;font-family:"Roboto",Arial,sans-serif;}
  .card{position:absolute;top:30px;}
  .card--front{left:336px;width:253px;height:434px;}
  .card--back{left:620px;top:34px;width:243px;height:425px;}
  .card svg{display:block;width:100%;height:100%;}
  .side-label{position:absolute;top:500px;font-weight:700;font-size:15px;color:var(--ink);letter-spacing:.3px;}
  .side-label--front{left:436px;}
  .side-label--back{left:717px;}
  .brand-name{font-family:"Roboto",Arial,sans-serif;font-weight:900;fill:var(--blue);}
  .address{font-weight:700;font-size:35px;fill:var(--ink);}
  .web{font-weight:700;font-size:28px;fill:var(--ink);}
  .phone-number{font-weight:700;font-size:35px;fill:#ffffff;}
  .meal{font-weight:700;font-size:34px;fill:var(--yellow);}
</style>
</head>
<body>
<main class="sheet">

  <section class="card card--front" aria-label="Card front">
    <svg viewBox="0 0 460 790" xmlns="http://www.w3.org/2000/svg">
      <rect class="frame" x="0" y="0" width="460" height="790" rx="62" fill="var(--orange)"/>
      <rect class="panel" x="18" y="18" width="424" height="754" rx="46" fill="var(--yellow)"/>

      <text class="brand-name" x="230" y="112" font-size="66" text-anchor="middle">SALT REEF</text>
      <text class="brand-name" x="230" y="195" font-size="80" text-anchor="middle">CAFE</text>

      <g class="pin-icon" transform="translate(227,255)">
        <path d="M0 70 L-20 30 A22 22 0 1 1 20 30 Z" fill="var(--blue)"/>
        <circle cx="0" cy="18" r="10" fill="var(--orange)" stroke="var(--yellow)" stroke-width="3"/>
      </g>

      <text class="address" x="228" y="360" text-anchor="middle">117 Parade</text>
      <text class="address" x="228" y="403" text-anchor="middle">Coralby SA 5172</text>

      <line class="divider" x1="125" y1="463" x2="347" y2="463" stroke="var(--blue)" stroke-width="5"/>

      <text class="web" x="230" y="535" text-anchor="middle">Menu &amp; Opening Hours</text>
      <text class="web" x="228" y="572" text-anchor="middle">www.saltreefcafe.com.au</text>

      <g class="phone-pill">
        <rect x="95" y="655" width="323" height="62" rx="14" fill="var(--blue)"/>
        <circle cx="85" cy="686" r="38" fill="var(--orange)"/>
        <path d="M72 668 q-6 4 -2 16 q6 16 22 22 q8 3 12 -2 l-8 -8 q-4 3 -8 0 q-6 -5 -9 -12 q-2 -4 2 -6 z" fill="#ffffff"/>
        <text class="phone-number" x="146" y="698">(08) 8461 9273</text>
      </g>
    </svg>
  </section>

  <section class="card card--back" aria-label="Card back">
    <svg viewBox="0 0 441 773" xmlns="http://www.w3.org/2000/svg">
      <defs>
        <clipPath id="back-shape"><rect width="441" height="773" rx="46"/></clipPath>
      </defs>
      <g clip-path="url(#back-shape)">
        <rect class="base" width="441" height="773" fill="var(--yellow)"/>
        <path class="band" d="M117 0 H323 V450 Q323 500 360 550 L441 635 V773 H0 V635 L80 550 Q117 500 117 450 Z" fill="var(--blue)"/>
      </g>

      <g class="clock" transform="translate(220,75)">
        <circle r="53" fill="var(--orange)" stroke="var(--yellow)" stroke-width="3"/>
        <g fill="var(--yellow)"><circle cy="-42" r="3"/><circle cy="42" r="3"/><circle cx="-42" r="3"/><circle cx="42" r="3"/></g>
        <path d="M0 0 V-34 M0 0 L-14 12" stroke="var(--yellow)" stroke-width="4" stroke-linecap="round"/>
        <circle r="4" fill="var(--blue)"/>
      </g>
      <text class="meal" x="220" y="175" text-anchor="middle">Breakfast</text>

      <g class="clock" transform="translate(220,258)">
        <circle r="53" fill="var(--orange)" stroke="var(--yellow)" stroke-width="3"/>
        <g fill="var(--yellow)"><circle cy="-42" r="3"/><circle cy="42" r="3"/><circle cx="-42" r="3"/><circle cx="42" r="3"/></g>
        <path d="M0 0 V-34 M0 0 L-8 -20" stroke="var(--yellow)" stroke-width="4" stroke-linecap="round"/>
        <circle r="4" fill="var(--blue)"/>
      </g>
      <text class="meal" x="220" y="358" text-anchor="middle">Lunch</text>

      <g class="clock" transform="translate(220,445)">
        <circle r="53" fill="var(--orange)" stroke="var(--yellow)" stroke-width="3"/>
        <g fill="var(--yellow)"><circle cy="-42" r="3"/><circle cy="42" r="3"/><circle cx="-42" r="3"/><circle cx="42" r="3"/></g>
        <path d="M0 0 V-34 M0 0 L10 20" stroke="var(--yellow)" stroke-width="4" stroke-linecap="round"/>
        <circle r="4" fill="var(--blue)"/>
      </g>
      <text class="meal" x="220" y="543" text-anchor="middle">Dinner</text>

      <circle class="coffee-icon" cx="110" cy="635" r="53" fill="var(--orange)" stroke="var(--yellow)" stroke-width="3" role="img" aria-label="Steaming coffee cup icon"/>
      <text class="meal" x="110" y="732" text-anchor="middle">Coffee</text>

      <circle class="takeaway-icon" cx="313" cy="635" r="53" fill="var(--orange)" stroke="var(--yellow)" stroke-width="3" role="img" aria-label="Takeaway bag icon"/>
      <text class="meal" x="313" y="732" text-anchor="middle">Takeaway</text>
    </svg>
  </section>

  <div class="side-label side-label--front">SIDE A</div>
  <div class="side-label side-label--back">SIDE B</div>
</main>
</body>
</html>
```